mno school poster design and change logo name

We already have a logo which only needs to be slightly modified with "school".
We also have two advertising faces, a girl and a boy, which should be on our poster.
Important key data:

bilingual D/E small classes
daycare
private kindergarten
private school from 2024

Poster size: 268,5 x 128 cm
We need logo sizes in different sizes
also for T-shirts.
Attached also a old poster

Target Market(s)

new clients

Colors
0094D4
00A9DD
6FCCEA
C7EBF8
E9F6FB
59FF00
82FF00
B8FF75
E3FFCB
F4FFEA
FFC000
F8CF3A
FAE287
FDF2CF
FEFAEE
F0912C
F2A743
F7CA91
FBE8D2
FDF5EE

```html
<!DOCTYPE html>
<html lang="en">
<head>
<meta charset="utf-8">
<title>mno School – Poster</title>
<link href="https://fonts.googleapis.com/css2?family=Comic+Neue:wght@400;700&display=swap" rel="stylesheet">
<style>
  :root {
    --page: #ebebeb;
    --sky: #def5fc;
    --pink: #f4489c;
    --blue: #0094d4;
    --orange: #f7a000;
    --lime: #bbd200;
    --sun: #f8cf3a;
    --ink: #111111;
    --white: #ffffff;
  }
  * { margin: 0; padding: 0; box-sizing: border-box; }
  html, body {
    width: 1200px;
    height: 679px;
    overflow: hidden;
    background: var(--page);
    font-family: "Comic Neue", "Comic Sans MS", cursive;
  }
  .poster {
    position: absolute;
    left: 0;
    top: 53px;
    width: 1200px;
    height: 572px;
    background: var(--sky);
    overflow: hidden;
  }
  .poster__shapes {
    position: absolute;
    inset: 0;
  }
  .poster__visual {
    position: absolute;
    left: 590px;
    top: 118px;
    width: 510px;
    height: 454px;
    border-radius: 255px 255px 0 0;
    background: radial-gradient(circle at 55% 60%, #f3c9a8 0%, #e9b07a 30%, #f7b733 55%, rgba(248, 207, 58, 0) 75%);
  }
  .brand {
    position: absolute;
    left: 945px;
    top: 96px;
    width: 235px;
    display: flex;
    align-items: center;
    justify-content: center;
    gap: 10px;
    white-space: nowrap;
  }
  .brand__dot {
    width: 22px;
    height: 22px;
    border-radius: 50%;
    background: var(--sun);
    flex: none;
  }
  .brand__name {
    font-size: 40px;
    font-weight: 700;
    color: var(--orange);
    line-height: 1;
  }
  .headline {
    position: absolute;
    left: 34px;
    width: 530px;
    text-align: center;
    font-weight: 700;
    line-height: 1;
    white-space: nowrap;
  }
  .headline--school {
    top: 198px;
    font-size: 80px;
    color: var(--blue);
  }
  .headline--year {
    top: 278px;
    font-size: 82px;
    color: var(--orange);
    letter-spacing: 2px;
  }
  .pill {
    position: absolute;
    height: 58px;
    border-radius: 29px;
    display: flex;
    align-items: center;
    justify-content: center;
    color: var(--white);
    font-weight: 700;
    line-height: 1;
    white-space: nowrap;
  }
  .pill--bilingual { left: 34px; top: 363px; width: 531px; font-size: 41px; background: var(--pink); }
  .pill--kindergarten { left: 34px; top: 431px; width: 361px; font-size: 37px; background: var(--orange); }
  .pill--daycare { left: 404px; top: 431px; width: 161px; font-size: 37px; background: var(--lime); }
  .website {
    position: absolute;
    left: 34px;
    top: 512px;
    width: 531px;
    text-align: center;
    font-size: 30px;
    line-height: 1;
    letter-spacing: 5px;
    color: var(--ink);
  }
</style>
</head>
<body>
  <main class="poster">
    <svg class="poster__shapes" width="1200" height="572" viewBox="0 0 1200 572" aria-hidden="true">
      <path d="M0 0 H492 C510 50 480 100 420 95 C360 90 310 40 250 60 C190 80 190 200 80 195 C40 193 15 185 0 180 Z" fill="var(--pink)"/>
      <path d="M15 0 C20 100 60 120 150 115 C230 110 250 50 340 55 C420 60 460 95 510 75 C525 60 522 20 520 0" fill="none" stroke="var(--white)" stroke-width="2" stroke-dasharray="8 6"/>
      <path d="M1200 267 C1150 260 1110 270 1095 320 C1080 370 1095 420 1050 470 C1020 505 1000 540 1000 572 H1200 Z" fill="var(--lime)"/>
      <path d="M1200 230 C1120 270 1140 330 1130 390 C1120 450 1060 480 1020 520" fill="none" stroke="var(--white)" stroke-width="2" stroke-dasharray="8 6"/>
    </svg>

    <div class="poster__visual" role="img" aria-label="Smiling girl with rainbow-painted hands, wearing a paper crown, in front of an orange sun with a kite and clouds"></div>

    <div class="brand">
      <span class="brand__dot"></span>
      <span class="brand__name">mno School</span>
    </div>

    <h1 class="headline headline--school">Private School</h1>
    <p class="headline headline--year">from 2024</p>
    <p class="pill pill--bilingual">Bilingual D/E small classes</p>
    <p class="pill pill--kindergarten">Private Kindergarten</p>
    <p class="pill pill--daycare">Daycare</p>
    <p class="website">www.mno-daycare.ch</p>
  </main>
</body>
</html>
```